Specialised investor in e-mobility and energy wants business card design

We need a business card design that fits our existing corporate design. <The look and feel must be 'sharp'/'clean', dynamic, communicate momentum, professionalism etc (as one would imagine from a firm in the financial sector). We like the idea of a reverse-side of the card that includes the logo, and the name and contact details on the other. We expect the deliverable to be whatever format might be required to be able to get cards printed directly by a service such as tandor press. Our website is www.orm.capital

```html
<!DOCTYPE html>
<html lang="en">
<head>
<meta charset="utf-8">
<title>ORM Capital – Business Card</title>
<link rel="stylesheet" href="https://fonts.googleapis.com/css2?family=Arimo:wght@400;700&display=swap">
<style>
  :root {
    --backdrop: #121312;
    --card: #264a1d;
    --card-deep: #223f1a;
    --edge: #6aa336;
    --accent: #6fae38;
    --ink: #ffffff;
    --emboss: #2f5a24;
  }
  * { box-sizing: border-box; margin: 0; padding: 0; }
  html, body { width: 1200px; height: 963px; overflow: hidden; }
  body {
    background: var(--backdrop);
    font-family: "Arimo", Arial, sans-serif;
    display: flex;
    flex-direction: column;
    align-items: center;
    justify-content: center;
    gap: 60px;
  }
  .card {
    position: relative;
    width: 620px;
    height: 354px;
    border-radius: 22px;
    background: linear-gradient(160deg, var(--card) 0%, var(--card-deep) 100%);
    box-shadow: 0 0 0 2px var(--edge), 0 18px 40px rgba(0,0,0,.55);
    overflow: hidden;
  }
  /* Front */
  .front .wordmark {
    position: absolute;
    top: 118px;
    left: 250px;
    font-size: 44px;
    font-weight: 400;
    color: var(--ink);
    letter-spacing: 1px;
  }
  .front .wordmark-dot {
    position: absolute;
    top: 131px;
    left: 222px;
    width: 18px;
    height: 18px;
    border-radius: 50%;
    background: var(--accent);
  }
  .identity {
    position: absolute;
    left: 60px;
    top: 236px;
    width: 200px;
    text-align: right;
  }
  .identity .name {
    font-size: 15px;
    font-weight: 700;
    color: var(--ink);
    letter-spacing: .5px;
  }
  .identity .name .surname { color: var(--accent); }
  .identity .place {
    margin-top: 4px;
    font-size: 14px;
    color: var(--ink);
  }
  .divider {
    position: absolute;
    left: 282px;
    top: 226px;
    width: 1px;
    height: 82px;
    background: var(--ink);
    opacity: .8;
  }
  .contacts {
    position: absolute;
    left: 302px;
    top: 230px;
    list-style: none;
  }
  .contacts li {
    display: flex;
    align-items: center;
    gap: 10px;
    font-size: 14px;
    color: var(--ink);
    line-height: 25px;
  }
  .contacts svg { width: 14px; height: 14px; flex: none; }
  /* Back */
  .back .wordmark {
    position: absolute;
    inset: 0;
    display: flex;
    align-items: center;
    justify-content: center;
    font-size: 58px;
    font-weight: 400;
    color: var(--emboss);
    letter-spacing: 1px;
  }
</style>
</head>
<body>
  <section class="card front" aria-label="Business card front">
    <span class="wordmark-dot"></span>
    <div class="wordmark">ORM Capital</div>

    <div class="identity">
      <p class="name">MARCUS <span class="surname">FELDBERG</span></p>
      <p class="place">Geneva, Switzerland</p>
    </div>

    <div class="divider"></div>

    <ul class="contacts">
      <li>
        <svg viewBox="0 0 16 16" aria-hidden="true"><path fill="#6fae38" d="M3.6 1.5l2.2 2.6-1.3 1.6c.8 1.8 2.2 3.3 4 4.1l1.6-1.3 2.6 2.2-1.2 2.3C6.3 12.7 3.3 9.7 1.5 4.5z"/></svg>
        +41 79 555 0142
      </li>
      <li>
        <svg viewBox="0 0 16 16" aria-hidden="true"><rect x="1" y="3.5" width="14" height="9" rx="1" fill="#6fae38"/><path d="M1.5 4l6.5 5 6.5-5" fill="none" stroke="#264a1d" stroke-width="1.2"/></svg>
        marcus@orm.capital
      </li>
      <li>
        <svg viewBox="0 0 16 16" aria-hidden="true"><circle cx="8" cy="8" r="6.5" fill="#6fae38"/><path d="M1.5 8h13M8 1.5c-2.6 3-2.6 10 0 13M8 1.5c2.6 3 2.6 10 0 13" fill="none" stroke="#264a1d" stroke-width="1"/></svg>
        www.orm.capital
      </li>
    </ul>
  </section>

  <section class="card back" aria-label="Business card back">
    <div class="wordmark">ORM Capital</div>
  </section>
</body>
</html>
```